Software Company Business Card Design

We are looking for a business card design for a software, messaging & IT services company based in Australia.

Talvora Group is the holding company for 3 brands all offering technology based business solutions; Talvora, Brindle & Quillpad. Brand Identity = Friendly, Professional, Viable, Vibrant, Creative

We want our business card to reflect that we are an innovative market leader. The design should be clean, professional and original.

This design will be used for all 3 brands.

More information about our company can be found at: www.talvoragroup.example.au
www.brindle.example.au

Details we would like on the card:

Firstname Lastname
Position
Level 17, 482 Ormond Rd
North Sydney
NSW 2060
Phone: +61 2 5550 1738
Fax: +61 2 5550 1794
Mobile:
Email:
www.talvoragroup.example.au

Target Market(s)

Our business cards are given to B2B and industry professionals.

Industry/Entity Type

Business

Requirements
Must have
• The Business Card must include the same colours as the logo.
Nice to have
• We would like it to me double sided.

```html
<!DOCTYPE html>
<html lang="en">
<head>
<meta charset="utf-8">
<title>Talvora Group – Business Cards</title>
<link href="https://fonts.googleapis.com/css2?family=Questrial&display=swap" rel="stylesheet">
<style>
  :root {
    --backdrop: #2b2b2b;
    --card-light: #f4f4f4;
    --card-mid: #e2e2e2;
    --brand-crimson: #b0123e;
    --brand-lavender: #8b8aa6;
    --text-dark: #474747;
    --text-mid: #5a5a5a;
    --web-slate: #555a72;
  }
  * { margin: 0; padding: 0; box-sizing: border-box; }
  html, body {
    width: 1200px; height: 719px; overflow: hidden;
    background: var(--backdrop);
    font-family: "Questrial", "Century Gothic", sans-serif;
  }
  .stage { position: relative; width: 1200px; height: 719px; }

  .card {
    position: absolute;
    background: radial-gradient(ellipse at 30% 15%, #ffffff 0%, var(--card-light) 35%, var(--card-mid) 100%);
  }
  .card--front { left: 65px; top: 271px; width: 396px; height: 238px; }
  .card--back  { left: 485px; top: 271px; width: 396px; height: 238px;
    background: radial-gradient(ellipse at 45% 10%, #ffffff 0%, #efefef 40%, #d9d9d9 100%); }
  .card--tall  { left: 905px; top: 113px; width: 237px; height: 396px;
    background: radial-gradient(ellipse at 50% 75%, #ffffff 0%, #f1f1f1 40%, #e3e3e3 100%); }

  .wordmark {
    position: absolute;
    color: var(--brand-crimson);
    font-weight: 400;
    letter-spacing: -0.5px;
    white-space: nowrap;
    line-height: 1;
  }
  .card--front .wordmark { left: 36px; top: 96px; font-size: 24px; }
  .card--back .wordmark  { left: 0; width: 100%; text-align: center; top: 96px; font-size: 34px; }
  .card--tall .wordmark  { left: 0; width: 100%; text-align: center; top: 306px; font-size: 29px; }

  .divider {
    position: absolute; left: 184px; top: 52px; width: 2px; height: 118px;
    background: linear-gradient(to bottom, rgba(0,0,0,0), rgba(0,0,0,0.22), rgba(0,0,0,0));
  }
  .contact { position: absolute; left: 196px; top: 52px; color: var(--text-dark); white-space: nowrap; }
  .contact__name { font-size: 18px; font-weight: 700; }
  .contact__role { font-size: 13px; color: var(--text-mid); margin-top: 1px; font-weight: 700; }
  .contact__lines { margin-top: 8px; font-size: 12.5px; line-height: 15px; font-weight: 700; }
  .contact__label { color: var(--brand-lavender); }
  .contact__address { font-size: 10px; line-height: 13px; }

  .web {
    position: absolute; left: 0; top: 174px; width: 100%; text-align: center;
    font-size: 12px; letter-spacing: 3.4px; color: var(--web-slate); font-weight: 700;
    white-space: nowrap;
  }
  .web__brand { color: var(--brand-crimson); }
</style>
</head>
<body>
<main class="stage">
  <section class="card card--front" aria-label="Card front">
    <div class="wordmark">talvora group</div>
    <div class="divider"></div>
    <div class="contact">
      <div class="contact__name">Firstname Lastname</div>
      <div class="contact__role">position</div>
      <div class="contact__lines">
        <div><span class="contact__label">P:</span> +61 2 5550 1738</div>
        <div><span class="contact__label">F:</span> +61 2 5550 1794</div>
        <div><span class="contact__label">A:</span> <span class="contact__address">Level 17, 482 Ormond Rd</span></div>
        <div class="contact__address">Wexley Park NSW 2183</div>
      </div>
    </div>
  </section>

  <section class="card card--back" aria-label="Card back">
    <div class="wordmark">talvora group</div>
    <div class="web">www.<span class="web__brand">talvoragroup</span>.example.au</div>
  </section>

  <section class="card card--tall" aria-label="Vertical card">
    <div class="wordmark">talvora group</div>
  </section>
</main>
</body>
</html>
```